Teachers workshop flyer

I need a flyer to inform schools of a workshop for teachers that empowers the teacher to help traumatised and disadvantaged students to engage in successful learning.

I am a teacher and educator and my info for the flyer is attached.

Target Market(s)

Principals and vice-principals who have stressed staff and students and they want things to be better in the school!

Industry/Entity Type

Teacher

```html
<!DOCTYPE html>
<html lang="en">
<head>
<meta charset="utf-8">
<title>Brain-Based Strategies for Student Success</title>
<link rel="stylesheet" href="https://fonts.googleapis.com/css2?family=Cabin+Sketch:wght@400;700&family=Carlito:ital,wght@0,400;0,700;1,400;1,700&display=swap">
<style>
  :root {
    --brick-dark: #4a2a1e;
    --brick-mid: #7a4a35;
    --brick-light: #a6715a;
    --board: #2b2b2b;
    --board-light: #3a3a3a;
    --frame: #b07a45;
    --frame-dark: #8a5a2e;
    --chalk: #f2f2f2;
    --orange: #f58220;
    --orange-deep: #e86a10;
    --ink: #1e1e1e;
    --quote-grey: #8c8c8c;
    --footer: #262626;
    --white: #ffffff;
  }
  * { box-sizing: border-box; margin: 0; padding: 0; }
  html, body { width: 846px; height: 1200px; overflow: hidden; background: var(--white); }
  .flyer {
    position: relative; width: 846px; height: 1200px; overflow: hidden;
    font-family: "Carlito", "Calibri", sans-serif; color: var(--ink);
  }
  .hero { position: absolute; left: 0; top: 0; width: 846px; height: 580px; }
  .hero svg { display: block; }
  .title {
    position: absolute; left: 132px; top: 128px;
    font-family: "Cabin Sketch", cursive; font-weight: 400;
    color: var(--chalk); text-transform: uppercase; letter-spacing: 3px;
    line-height: 1;
  }
  .title span { display: block; font-size: 58px; margin-bottom: 6px; }
  .title .title-small { font-size: 42px; margin: 4px 0 8px; }
  .intro {
    position: absolute; left: 48px; top: 590px; width: 752px;
    font-size: 15.2px; line-height: 1.38;
  }
  .intro p + p { margin-top: 12px; }
  .presenter {
    position: absolute; left: 38px; top: 734px; width: 768px; height: 134px;
    background: var(--orange); border-radius: 14px;
    box-shadow: 0 3px 5px rgba(0,0,0,0.25);
    padding: 8px 16px 0 16px; color: var(--white);
  }
  .presenter-heading {
    display: inline-block; font-weight: 700; font-style: italic; font-size: 15.5px;
    margin-bottom: 10px;
  }
  .presenter p { font-weight: 700; font-style: italic; font-size: 14.4px; line-height: 1.36; }
  .feedback { position: absolute; left: 0; top: 872px; width: 846px; height: 100px; }
  .quote-mark {
    position: absolute; font-family: Georgia, serif; font-weight: 700;
    color: var(--quote-grey); font-size: 190px; line-height: 1;
  }
  .quote-open { left: 34px; top: -6px; }
  .quote-close { left: 760px; top: 10px; }
  .feedback-heading { position: absolute; left: 76px; top: 14px; font-weight: 700; font-size: 15.5px; }
  .feedback-text {
    position: absolute; left: 76px; top: 40px; width: 730px;
    font-weight: 700; font-size: 15.5px; line-height: 1.35;
  }
  .moments-label {
    position: absolute; left: 50px; top: 974px; width: 238px; height: 26px;
    background: var(--orange); border-radius: 13px;
    color: var(--white); font-weight: 700; font-size: 17px;
    padding: 3px 0 0 18px;
  }
  .moments {
    position: absolute; left: 66px; top: 1004px; list-style: none;
    font-weight: 700; font-size: 17.6px;
  }
  .moments li { position: relative; padding-left: 16px; height: 32px; line-height: 32px; }
  .moments li::before {
    content: ""; position: absolute; left: 0; top: 12px;
    width: 9px; height: 9px; border-radius: 50%; background: var(--orange);
  }
  .footer {
    position: absolute; left: 0; top: 1102px; width: 846px; height: 98px;
    background: var(--footer); color: var(--white); text-align: center;
    font-weight: 700;
  }
  .footer-line1 { margin-top: 14px; font-size: 16.5px; }
  .footer-line2 { margin-top: 6px; font-size: 16.5px; }
  .footer .big { font-size: 23px; }
</style>
</head>
<body>
<main class="flyer">
  <header class="hero">
    <svg width="846" height="580" viewBox="0 0 846 580" xmlns="http://www.w3.org/2000/svg">
      <defs>
        <linearGradient id="brickGrad" x1="0" y1="0" x2="1" y2="1">
          <stop offset="0" stop-color="#3e2218"/>
          <stop offset="0.5" stop-color="#8a5740"/>
          <stop offset="1" stop-color="#5a3325"/>
        </linearGradient>
        <radialGradient id="boardGrad" cx="0.5" cy="0.45" r="0.7">
          <stop offset="0" stop-color="#3b3b3b"/>
          <stop offset="1" stop-color="#202020"/>
        </radialGradient>
      </defs>
      <rect class="brick-wall" x="0" y="0" width="846" height="580" fill="url(#brickGrad)" role="img" aria-label="Photograph of a red brick wall behind the chalkboard"/>
      <rect class="board-frame" x="86" y="66" width="656" height="414" fill="var(--frame)" stroke="var(--frame-dark)" stroke-width="2"/>
      <rect class="board" x="98" y="78" width="632" height="390" fill="url(#boardGrad)"/>
      <rect class="bulb-doodle" x="548" y="124" width="140" height="236" rx="10" fill="#4a4a4a" opacity="0.6" role="img" aria-label="Chalk drawing of a light bulb with a trailing cord"/>
      <rect class="chalk-stick" x="176" y="468" width="86" height="10" fill="#e8e8e8"/>
      <path class="orange-swoosh" d="M0 548 C 250 560 560 540 846 470 L846 520 C 560 580 250 580 0 580 Z" fill="var(--orange)"/>
      <path class="white-curve" d="M0 562 C 250 575 560 560 846 500 L846 580 L0 580 Z" fill="var(--white)"/>
    </svg>
    <h1 class="title">
      <span>Brain-Based</span>
      <span>Strategies</span>
      <span class="title-small">for</span>
      <span>Student Success</span>
    </h1>
  </header>

  <section class="intro">
    <p>Contemporary teaching is a highly complex role as increasing numbers of students attend school without the essential ‘self-skills’ to be truly ‘school-ready’ and successful. Instead these students often seek-out attention in ways that can disruptive in the classroom causing stress and frustration for teachers.</p>
    <p>Dan shows how and why the most effective strategies for these students are guided by a sound understanding of child-development and brain-development - especially where trauma has left lasting impacts. Teachers can learn how to build a student’s self-skills, without the teacher having to become a therapist!</p>
  </section>

  <section class="presenter">
    <h2 class="presenter-heading">About the Presenter:</h2>
    <p>Daniel Marsh is a Melbourne-based therapist and educator with over twenty years experience working with adults and young people in the area of trauma and recovery. Dan’s seminars are engaging and practical since teachers need effective strategies that will immediately translate into classroom practice. Dan has trained here and overseas in the most effective behavior change strategies.</p>
  </section>

  <section class="feedback">
    <span class="quote-mark quote-open" aria-hidden="true">“</span>
    <span class="quote-mark quote-close" aria-hidden="true">”</span>
    <h2 class="feedback-heading">Teacher Feedback:</h2>
    <p class="feedback-text">Dan was such an engaging and energetic presenter whom I enjoyed immensely. His presentation on the brain and take away strategies were so practical and meaningful. It was an invaluable session.</p>
  </section>

  <h2 class="moments-label">My Light-bulb moments:</h2>
  <ul class="moments">
    <li>I need to CONNECT – not correct – far more often.</li>
    <li>Seeing negative self-talk for what it is.</li>
    <li>Using far more ‘diversions’ in the avoidance loop.”</li>
  </ul>

  <footer class="footer">
    <p class="footer-line1"><span class="big">Call 0400 123 456</span> for more information or</p>
    <p class="footer-line2">to book Dan to come to your school: <span class="big">www.danielmarsh.com.au/studentsuccess</span></p>
  </footer>
</main>
</body>
</html>
```